ROLL-ON-VERANDA Business Card Design

Please do not submit more than one design per designer. Both the front and the back must be submitted as a single design. Please use all of the attached files to design a two-sided business card. Do not use tiny text that is hard to read. Do not put text or images too close to the edges where it might get cut off during printing. The card should be horizontal. Please do not send me the same design that I attached showing the business information. Be creative.

One file is marked as the primary logo for company. Other files are marked as secondary. All logos should be incorporated into the design with a focus on the primary one being bigger.

```html
<!DOCTYPE html>
<html lang="en">
<head>
<meta charset="utf-8">
<title>ROLL-ON-VERANDA Business Card</title>
<link rel="stylesheet" href="https://fonts.googleapis.com/css2?family=Russo+One&family=Arimo:wght@400;700&display=swap">
<style>
  :root {
    --ink: #0d0d0d;
    --paper: #ffffff;
    --backdrop: #c9c9cb;
    --grey-text: #3a3a3a;
    --badge-navy: #1d2b6b;
    --badge-red: #c8202d;
    --badge-gold: #c99a2e;
    --badge-steel: #5e8fb8;
  }
  * { box-sizing: border-box; margin: 0; padding: 0; }
  html, body { width: 1200px; height: 800px; overflow: hidden; }
  body {
    background: var(--backdrop);
    font-family: "Arimo", Arial, sans-serif;
    position: relative;
  }
  .card {
    position: absolute;
    width: 600px;
    height: 343px;
    left: 300px;
    background: var(--paper);
    border-radius: 22px;
    overflow: hidden;
    box-shadow: 0 10px 24px rgba(0,0,0,0.22);
  }
  .card--front { top: 32px; }
  .card--back { top: 425px; }

  /* Front */
  .front-band { position: absolute; inset: 0; }
  .front-boat {
    position: absolute;
    left: 370px; top: 54px;
    width: 200px; height: 96px;
    border-radius: 40% 60% 30% 20% / 50% 60% 40% 50%;
    background: linear-gradient(160deg, #f2f2f2 0%, #8a8a8a 45%, #111 100%);
  }
  .front-phone {
    position: absolute;
    right: 34px; top: 24px;
    font-size: 17px;
    color: var(--ink);
    letter-spacing: 0.5px;
  }
  .wordmark {
    font-family: "Russo One", sans-serif;
    color: var(--ink);
    line-height: 1;
  }
  .front-wordmark {
    position: absolute;
    left: 40px; top: 118px;
    font-size: 26px;
  }
  .wordmark .dotcom {
    display: block;
    text-align: right;
    font-size: 12px;
    margin-top: 2px;
  }
  .front-details {
    position: absolute;
    left: 40px; top: 208px;
    color: var(--paper);
  }
  .credentials { list-style: none; font-size: 14px; line-height: 1.2; }
  .captain-name {
    font-family: "Russo One", sans-serif;
    font-size: 20px;
    letter-spacing: 0.5px;
    margin-top: 7px;
  }
  .email { font-size: 15px; margin-top: 3px; }

  /* Back */
  .back-boat {
    position: absolute;
    left: 70px; top: 38px;
    width: 200px; height: 70px;
    border-radius: 50% 50% 40% 40% / 60% 60% 40% 40%;
    background: linear-gradient(170deg, #e8e8e8 0%, #7b7b7b 50%, #1a1a1a 100%);
  }
  .back-wordmark {
    position: absolute;
    left: 46px; top: 118px;
    font-size: 30px;
  }
  .services {
    position: absolute;
    left: 46px; top: 200px;
    list-style: none;
    font-family: "Russo One", sans-serif;
    font-size: 15px;
    color: var(--grey-text);
    letter-spacing: 1px;
    line-height: 1.9;
  }
  .services li::before {
    content: "";
    display: inline-block;
    width: 7px; height: 7px;
    border-radius: 50%;
    background: var(--ink);
    margin-right: 14px;
    vertical-align: middle;
  }
  .badges {
    position: absolute;
    right: 36px; top: 34px;
    display: flex;
    flex-direction: column;
    gap: 14px;
  }
  .badge { width: 56px; height: 56px; border-radius: 50%; }
  .badge--guard { background: var(--badge-navy); }
  .badge--council { background: var(--paper); border: 4px solid var(--badge-steel); }
  .badge--veteran { background: var(--badge-red); border: 4px solid var(--badge-navy); }
  .badge--training { background: var(--paper); border: 5px solid var(--badge-gold); }
</style>
</head>
<body>
  <section class="card card--front">
    <svg class="front-band" viewBox="0 0 600 343" aria-hidden="true">
      <path d="M0,343 L0,196 C100,184 250,178 360,166 C460,152 540,128 600,108 L600,343 Z" fill="var(--ink)"/>
      <path d="M20,190 C120,176 260,172 360,160 C250,166 120,172 20,190 Z" fill="var(--paper)"/>
    </svg>
    <div class="front-boat" role="img" aria-label="Line illustration of a centre-console motorboat on the water"></div>
    <p class="front-phone">(555)014-2290</p>
    <div class="wordmark front-wordmark">ROLL-ON-VERANDA<span class="dotcom">.COM</span></div>
    <div class="front-details">
      <ul class="credentials">
        <li>Veteran</li>
        <li>Graduate Degree</li>
        <li>NMSA Certified Instructor</li>
        <li>USCG Licensed Master Captain</li>
      </ul>
      <p class="captain-name">CAPTAIN DALE R. WHITFORD</p>
      <p class="email">service@rollonveranda.com</p>
    </div>
  </section>

  <section class="card card--back">
    <div class="back-boat" role="img" aria-label="Small motorboat illustration above the company name"></div>
    <div class="wordmark back-wordmark">ROLL-ON-VERANDA<span class="dotcom">.COM</span></div>
    <ul class="services">
      <li>PROVIDING HANDS-ON BOAT TRAINING</li>
      <li>CAPTAINING SERVICES AND</li>
      <li>DELIVERIES IN THE BAYSHORE COUNTY AREA.</li>
    </ul>
    <div class="badges">
      <div class="badge badge--guard" role="img" aria-label="Licensed captain certification badge"></div>
      <div class="badge badge--council" role="img" aria-label="Boating safety instructor badge"></div>
      <div class="badge badge--veteran" role="img" aria-label="Veteran-owned business badge"></div>
      <div class="badge badge--training" role="img" aria-label="Boat training and charters badge"></div>
    </div>
  </section>
</body>
</html>
```